New business card design to go with our new logo

just want an eye-catching business card to go with our new logo. We are open to double sided or single sided. Just want it to have the following info on it. Whatever layout you think looks best.

First and Last Name
Title
Phone 801-555-0187
Address 312 W. Larkmoor Avenue Orem UT 84057
Email thecrew@meadowstailandkennel.example

Industry/Entity Type

Business

```html
<!DOCTYPE html>
<html lang="en">
<head>
<meta charset="utf-8">
<title>Meadows Tail &amp; Kennel – Business Card</title>
<link rel="stylesheet" href="https://fonts.googleapis.com/css2?family=Fira+Sans:wght@400;500&family=Roboto:wght@400;500&display=swap">
<style>
  :root {
    --page: #b4b4b4;
    --card: #f1f1f1;
    --card-edge: #e4e4e4;
    --blue: #1596cf;
    --orange: #e0864a;
    --ink: #3a3a3a;
    --faint: rgba(0, 0, 0, 0.05);
  }
  * { box-sizing: border-box; margin: 0; padding: 0; }
  html, body { width: 1200px; height: 576px; overflow: hidden; }
  body {
    background: var(--page);
    position: relative;
    font-family: "Roboto", sans-serif;
  }
  .card {
    position: absolute;
    top: 138px;
    height: 293px;
    background: linear-gradient(180deg, var(--card), var(--card-edge));
    border-radius: 12px;
    overflow: hidden;
  }
  .card--front { left: 82px; width: 484px; }
  .card--back { left: 602px; width: 481px; }

  .backdrop-mark {
    position: absolute;
    border-radius: 50%;
    background: var(--faint);
  }
  .card--front .backdrop-mark { left: -30px; top: 10px; width: 230px; height: 260px; }
  .card--back .backdrop-mark { right: -40px; top: 70px; width: 200px; height: 230px; }

  .wordmark {
    position: absolute;
    display: flex;
    align-items: center;
    gap: 12px;
    font-family: "Roboto", sans-serif;
    font-weight: 500;
    color: var(--orange);
    white-space: nowrap;
  }
  .wordmark__dot {
    border-radius: 50%;
    background: var(--blue);
    flex: none;
  }
  .card--front .wordmark {
    left: 0; right: 0; top: 120px;
    justify-content: center;
    font-size: 30px;
  }
  .card--front .wordmark__dot { width: 46px; height: 46px; }
  .card--back .wordmark {
    left: 20px; top: 120px;
    font-size: 25px;
  }
  .card--back .wordmark__dot { width: 58px; height: 58px; }

  .wave { position: absolute; left: 0; top: 0; width: 481px; height: 150px; }

  .holder {
    position: absolute;
    right: 21px; top: 22px;
    text-align: right;
    color: #fff;
    font-family: "Fira Sans", sans-serif;
  }
  .holder__name { font-size: 19px; font-weight: 500; }
  .holder__title { font-size: 11px; margin-top: 5px; }

  .contacts {
    position: absolute;
    left: 22px; top: 217px;
    list-style: none;
    font-size: 12.5px;
    color: var(--ink);
  }
  .contacts li { display: flex; align-items: center; gap: 14px; height: 18px; }
  .contacts svg { width: 10px; height: 10px; fill: var(--orange); flex: none; }
  .contacts .accent { color: var(--blue); }

  .address {
    position: absolute;
    right: 21px; top: 235px;
    text-align: right;
    font-size: 12.5px;
    line-height: 18px;
    color: var(--ink);
  }
</style>
</head>
<body>

<section class="card card--front">
  <div class="backdrop-mark" aria-hidden="true"></div>
  <div class="wordmark">
    <span class="wordmark__dot"></span>
    <span class="wordmark__name">Meadows Tail &amp; Kennel</span>
  </div>
</section>

<section class="card card--back">
  <div class="backdrop-mark" aria-hidden="true"></div>
  <svg class="wave" viewBox="0 0 481 150" aria-hidden="true">
    <path fill="var(--blue)" d="M0 0 H481 V122 C410 116 350 80 290 48 C220 12 110 10 0 30 Z"/>
    <path fill="var(--orange)" d="M0 40 C110 14 210 18 290 58 C350 88 410 122 481 126 V135 C405 132 345 102 285 72 C205 34 100 34 0 58 Z"/>
  </svg>
  <div class="holder">
    <div class="holder__name">Jordan Ellis Reed</div>
    <div class="holder__title">Managing Director</div>
  </div>
  <div class="wordmark">
    <span class="wordmark__dot"></span>
    <span class="wordmark__name">Meadows Tail &amp; Kennel</span>
  </div>
  <ul class="contacts">
    <li>
      <svg viewBox="0 0 10 10" aria-hidden="true"><path d="M2 0 L4 2.5 L3 4 C3.8 5.5 4.6 6.3 6 7 L7.5 6 L10 8 L8.5 10 C4 9.5 0.5 6 0 1.5 Z"/></svg>
      <span>801-555-0187</span>
    </li>
    <li>
      <svg viewBox="0 0 10 10" aria-hidden="true"><circle cx="5" cy="5" r="4.5" fill="none" stroke="var(--orange)" stroke-width="1"/><path d="M0.5 5 H9.5 M5 0.5 C2.5 3 2.5 7 5 9.5 M5 0.5 C7.5 3 7.5 7 5 9.5" fill="none" stroke="var(--orange)" stroke-width="0.8"/></svg>
      <span>www.<span class="accent">meadowstailandkennel</span>.example</span>
    </li>
    <li>
      <svg viewBox="0 0 10 10" aria-hidden="true"><rect x="0" y="1.5" width="10" height="7"/><path d="M0 1.5 L5 5.5 L10 1.5" fill="none" stroke="#fff" stroke-width="0.8"/></svg>
      <span>thecrew@meadowstailandkennel.example</span>
    </li>
  </ul>
  <address class="address" style="font-style:normal">
    312 W. Larkmoor Avenue<br>Orem UT 84057
  </address>
</section>

</body>
</html>
```